Joan Pelley Letter Head

log and letter head

would like a modern feminine approch, please see attached the back of my business card

Joan Pelley Consulting

ABN 81 305 642 918

Address19a Brood Street Larkmoor Heights 5087 Coral Province

Business

```html
<!DOCTYPE html>
<html lang="en">
<head>
<meta charset="utf-8">
<title>Joan Pelley Consulting – Letterhead</title>
<link rel="stylesheet" href="https://fonts.googleapis.com/css2?family=Barlow:wght@400&family=Crimson+Text:wght@400;600&display=swap">
<style>
  :root {
    --paper: #ffffff;
    --brand-red: #e2252b;
    --ink: #1a1a1a;
    --signature-tone: #f1f1f1;
  }
  html, body {
    margin: 0;
    padding: 0;
    overflow: hidden;
    background: var(--paper);
  }
  .letterhead {
    position: relative;
    width: 848px;
    height: 1200px;
    overflow: hidden;
    background: var(--paper);
    color: var(--ink);
  }
  .brand {
    position: absolute;
    left: 496px;
    top: 50px;
    width: 280px;
    margin: 0;
    text-align: center;
    font-family: "Barlow", sans-serif;
    font-weight: 400;
    color: var(--brand-red);
  }
  .brand-name {
    display: block;
    font-size: 44px;
    line-height: 56px;
    white-space: nowrap;
  }
  .brand-line {
    display: block;
    margin-top: 4px;
    padding-left: 0.95em;
    font-size: 12px;
    line-height: 16px;
    letter-spacing: 0.95em;
    text-transform: uppercase;
    white-space: nowrap;
  }
  .sender-details {
    position: absolute;
    left: 536px;
    top: 150px;
    margin: 0;
    font-family: "Barlow", sans-serif;
    font-style: normal;
    font-size: 15px;
    line-height: 19.5px;
    color: var(--brand-red);
  }
  .sender-details .abn {
    display: block;
    margin-bottom: 6px;
  }
  .letter-title {
    position: absolute;
    left: 125px;
    top: 319px;
    margin: 0;
    font-family: "Crimson Text", serif;
    font-weight: 600;
    font-size: 19.4px;
    line-height: 26px;
    letter-spacing: 0.02em;
    text-transform: uppercase;
    white-space: nowrap;
  }
  .letter-body {
    position: absolute;
    left: 125px;
    top: 371px;
    width: 660px;
    font-family: "Crimson Text", serif;
    font-size: 18.4px;
    line-height: 22.2px;
    white-space: nowrap;
  }
  .letter-body p {
    margin: 0 0 14px;
  }
  .signature {
    position: absolute;
    left: 130px;
    top: 919px;
    width: 182px;
    height: 141px;
    background: var(--signature-tone);
  }
</style>
</head>
<body>
  <main class="letterhead">
    <header>
      <p class="brand">
        <span class="brand-name">Joan Pelley</span>
        <span class="brand-line">Consulting</span>
      </p>
      <address class="sender-details">
        <span class="abn">ABN 81 305 642 918</span>
        47c Tallow Street<br>
        Larkmoor Heights<br>
        5087 Coral Province
      </address>
    </header>

    <h1 class="letter-title">Letterhead design for Joan Pelley</h1>

    <section class="letter-body">
      <p>Nonsenist ulluptate peritasit as quam, essin este nem. Illorro con nis ea natiam<br>
      facea nossintus. Equi accae mo et occus cum iumqui aliquamet, si dolorrumqui<br>
      dolupicil ipsum quatusdae autaspe digenem et, offic to te et aut ipsus milit, il is<br>
      dolorum faci diatem res unt omnis aliquo minctis unturit volorro dolut volori-<br>
      busam intiore volupta tissimped es vollandi odite pos delest, con nos destius ducid<br>
      quis et quas aboratenit omnis in nempore volupta imporer untias rem inctota<br>
      turiandae.</p>
      <p>Inis de por rem quatemporunt fugia quam faceatios sinciuscit aboria cuptur sus<br>
      aliaestrum reperum dent est atur amusa veligent volorecta cus quibus ditatis<br>
      exeruntur, eseri assitatenest quam rest volorio resequam eos conestiae endae vide<br>
      volores sumquae cabori bea qui sero expedic iaectaquam quissit aestiundit officiis<br>
      pro volorum abor magnisci denditi volorro beariostiste escia corias dolupta com-<br>
      nit omnim eumquia tendelesciam labor ra dolluptiundi ut lantorehent evel eum<br>
      rem qui am nonsedi ationsectia corum harum repudam faccull anderum fugitas<br>
      volupitas.</p>
      <p>Nimostia evellendia aut aut etum que peri ate paruptur atur autem quo mi, ip-<br>
      suntus nos ipsa dit everio et ut as rem fuga. Mus et, sum sequoditium sum utendi-<br>
      aspid millam, aut volupta tincid ut ut quo ducim fugitat estinum delest harumque<br>
      nonsequibus volut eatempore, cuptam harion pra eatum qui nos possit res aut<br>
      volorersped que nos minient rae cum re de officil iquunti.</p>
    </section>

    <div class="signature" role="img" aria-label="Handwritten signature of the sender"></div>
  </main>
</body>
</html>
```